VR Business Card

Design new business cards for VELMOsoft

Please see attached for the design brief

**** Please note, please feel free to propose a font that works for a professional, technology company ***

Target Market(s)

Technology buyers

Industry/Entity Type

Business

```html
<!DOCTYPE html>
<html lang="en">
<head>
<meta charset="utf-8">
<title>VELMOsoft Business Card</title>
<link rel="stylesheet" href="https://fonts.googleapis.com/css2?family=Jost:wght@400;500;600&display=swap">
<style>
  :root {
    --backdrop: #7b6d6a;
    --navy: #1f3166;
    --white: #ffffff;
    --orange: #f0a02e;
    --card-shadow: rgba(0, 0, 0, 0.35);
  }
  html, body {
    margin: 0;
    padding: 0;
    width: 1200px;
    height: 803px;
    overflow: hidden;
    background: var(--backdrop);
    font-family: "Jost", "Futura", sans-serif;
  }
  .canvas {
    position: relative;
    width: 1200px;
    height: 803px;
  }
  .card {
    position: absolute;
    top: 68px;
    width: 429px;
    height: 275px;
    background: var(--white);
    box-shadow: 0 2px 6px var(--card-shadow);
    overflow: hidden;
  }
  .card-front { left: 110px; }
  .card-back { left: 651px; }

  /* front */
  .front-panel {
    position: absolute;
    left: 0; top: 0;
    width: 100%;
    height: 211px;
    background: var(--navy);
  }
  .holder-name {
    position: absolute;
    left: 245px; top: 22px;
    margin: 0;
    color: var(--white);
    font-size: 19px;
    font-weight: 600;
    letter-spacing: 0.8px;
  }
  .holder-role {
    position: absolute;
    left: 247px; top: 47px;
    margin: 0;
    color: var(--white);
    font-size: 13px;
    letter-spacing: 0.5px;
  }
  .contact-list {
    position: absolute;
    margin: 0;
    padding: 0;
    list-style: none;
    color: var(--white);
  }
  .contact-list li {
    display: flex;
    align-items: center;
    gap: 8px;
  }
  .contact-list svg { flex: none; }
  .front-contacts {
    left: 25px; top: 161px;
    font-size: 12px;
  }
  .front-contacts li { height: 18px; }
  .front-contacts .phone-line { font-size: 13px; letter-spacing: 0.4px; }

  .brand-name {
    position: absolute;
    margin: 0;
    color: var(--navy);
    font-weight: 500;
    text-transform: uppercase;
    letter-spacing: 1px;
    white-space: nowrap;
  }
  .front-brand {
    left: 32px; top: 226px;
    font-size: 19px;
  }

  .tagline {
    position: absolute;
    margin: 0;
    color: var(--orange);
    font-weight: 400;
    white-space: nowrap;
  }
  .front-tagline {
    right: 30px; top: 228px;
    font-size: 18px;
  }

  /* back */
  .back-panel {
    position: absolute;
    left: 0; top: 0;
    width: 192px;
    height: 100%;
    background: var(--navy);
  }
  .back-tagline {
    right: 22px; top: 15px;
    font-size: 18.5px;
  }
  .back-contacts {
    left: 27px; top: 126px;
    font-size: 13px;
    letter-spacing: 0.4px;
  }
  .back-contacts li { height: 16.5px; gap: 7px; }
  .company-address {
    position: absolute;
    left: 27px; top: 191px;
    margin: 0;
    color: var(--white);
    font-size: 12.5px;
    font-style: normal;
    line-height: 17.3px;
  }
  .back-brand {
    left: 192px; right: 0;
    top: 140px;
    text-align: center;
    font-size: 31px;
  }
  .website {
    position: absolute;
    left: 192px; right: 0;
    top: 207px;
    margin: 0;
    text-align: center;
    color: var(--navy);
    font-size: 12px;
    font-weight: 600;
  }
</style>
</head>
<body>
<main class="canvas">

  <section class="card card-front" aria-label="Business card front">
    <div class="front-panel"></div>
    <h1 class="holder-name">Daniel Hofer</h1>
    <p class="holder-role">CEO</p>
    <ul class="contact-list front-contacts">
      <li class="phone-line">
        <svg width="9" height="13" viewBox="0 0 9 13" aria-hidden="true">
          <rect x="1" y="0.5" width="7" height="12" rx="1.2" fill="none" stroke="#ffffff" stroke-width="1.2"/>
          <rect x="2.4" y="2" width="4.2" height="5" fill="#ffffff"/>
        </svg>
        <span>+41 795531207</span>
      </li>
      <li>
        <svg width="11" height="10" viewBox="0 0 11 10" aria-hidden="true">
          <rect x="0.5" y="2.5" width="10" height="7" fill="#ffffff"/>
          <path d="M0.5 2.5 L5.5 6.5 L10.5 2.5" fill="none" stroke="#1f3166" stroke-width="1"/>
        </svg>
        <span>daniel.hofer@velmosoft.ch</span>
      </li>
    </ul>
    <p class="brand-name front-brand">VELMOsoft</p>
    <p class="tagline front-tagline">...Built For What Is Next</p>
  </section>

  <section class="card card-back" aria-label="Business card back">
    <div class="back-panel"></div>
    <ul class="contact-list back-contacts">
      <li>
        <svg width="9" height="10" viewBox="0 0 9 10" aria-hidden="true">
          <path d="M2 0.5 C0.5 1.5 0.3 4 2.5 7 C4.5 9.5 6.8 10 8 8.8 L6.4 6.8 L5.2 7.4 C4 6.6 3 5 2.8 3.6 L3.9 2.8 Z" fill="#ffffff"/>
        </svg>
        <span>+41417260340</span>
      </li>
      <li>
        <svg width="9" height="10" viewBox="0 0 9 10" aria-hidden="true">
          <path d="M2 0.5 C0.5 1.5 0.3 4 2.5 7 C4.5 9.5 6.8 10 8 8.8 L6.4 6.8 L5.2 7.4 C4 6.6 3 5 2.8 3.6 L3.9 2.8 Z" fill="#ffffff"/>
        </svg>
        <span>+41417260341</span>
      </li>
      <li>
        <svg width="11" height="10" viewBox="0 0 11 10" aria-hidden="true">
          <rect x="3" y="0.5" width="6" height="4" fill="none" stroke="#ffffff" stroke-width="1"/>
          <rect x="0.5" y="4" width="10" height="6" fill="#ffffff"/>
          <rect x="2" y="5.5" width="2" height="3" fill="#1f3166"/>
        </svg>
        <span>+41800004518</span>
      </li>
    </ul>
    <address class="company-address">
      VELMOsoft Solutions AG,<br>
      Seeweg 8,<br>
      6300 Zug,<br>
      Switzerland
    </address>
    <p class="tagline back-tagline">...Built For What Is Next</p>
    <p class="brand-name back-brand">VELMOsoft</p>
    <p class="website">www.velmosoft.ch</p>
  </section>

</main>
</body>
</html>
```